Business card for a young aspring actress

My daughter is 18 and just starting out on her profession as an actress. She is a member of the Open Stage Company and has already had some extras work and a featured role in an upcoming Feature film.

She wants/needs a card that she can have to hand to give to those she comes into contact with in the theatre, TV and film industries.

We are thinking that it may be double sided with an impact side including a picture of her and her name etc with the reverse holding contact and other details.

She wants to go by the name Maren Joy Whitcombe.

She has done a little modelling but sees herself as an actress.

She can be seen in this video
http://www.hollybankacademy.example/videos/a3f19c7d5e2b8406c1d9e7f2a4b60835?width=640&height=480

Target Market(s)

Anyone she comes into contact with in theatre TV and film industries.

Industry/Entity Type

Business

Requirements
Nice to have
• She has email and a website www.marenwhitcombe.example She is quite a connected girl

```html
<!DOCTYPE html>
<html lang="en">
<head>
<meta charset="utf-8">
<title>Maren Joy Whitcombe — Business Card</title>
<link rel="stylesheet" href="https://fonts.googleapis.com/css2?family=Questrial&display=swap">
<style>
  :root {
    --backdrop: #b4b6b9;
    --card-back: #c8cacc;
    --ink-violet: #3a2f8f;
    --ink-grey: #55575b;
    --photo-light: #d9d9d9;
    --photo-mid: #9a9a9a;
    --photo-dark: #3e3e3e;
  }
  * { margin: 0; padding: 0; box-sizing: border-box; }
  html, body {
    width: 1200px;
    height: 900px;
    overflow: hidden;
  }
  body {
    position: relative;
    background: var(--backdrop);
    font-family: "Questrial", "Helvetica Neue", Arial, sans-serif;
  }

  /* Contact side */
  .card-back {
    position: absolute;
    left: 93px;
    top: 405px;
    width: 630px;
    height: 360px;
    border-radius: 40px;
    background: var(--card-back);
    text-align: center;
  }
  .card-back__name {
    position: absolute;
    left: 0;
    right: 0;
    top: 166px;
    font-size: 31px;
    font-weight: 400;
    color: var(--ink-violet);
    letter-spacing: 0.2px;
  }
  .card-back__contact {
    position: absolute;
    left: 0;
    right: 0;
    top: 229px;
    font-size: 17.5px;
    color: var(--ink-grey);
    letter-spacing: 0.3px;
  }
  .card-back__contact .divider { margin: 0 10px; }
  .social-list {
    position: absolute;
    left: 0;
    right: 0;
    top: 281px;
    display: flex;
    justify-content: center;
    gap: 18px;
    list-style: none;
    font-size: 14.5px;
    color: var(--ink-grey);
  }
  .social-list__item {
    display: flex;
    align-items: center;
    gap: 5px;
  }
  .social-list__mark {
    width: 13px;
    height: 13px;
    border-radius: 2px;
    background: var(--ink-violet);
  }

  /* Impact side */
  .card-front {
    position: absolute;
    left: 746px;
    top: 135px;
    width: 360px;
    height: 630px;
    border-radius: 36px;
    overflow: hidden;
  }
  .card-front__portrait {
    position: absolute;
    inset: 0;
    background:
      radial-gradient(ellipse 45% 40% at 48% 55%, var(--photo-light), transparent 70%),
      linear-gradient(90deg, var(--photo-dark) 0%, var(--photo-mid) 18%, var(--photo-light) 45%, var(--photo-mid) 80%, var(--photo-dark) 100%);
  }
  .card-front__name {
    position: absolute;
    left: 24px;
    bottom: 14px;
    font-size: 26px;
    line-height: 26.5px;
    color: var(--ink-violet);
    letter-spacing: 0.6px;
    text-transform: uppercase;
  }
</style>
</head>
<body>

  <section class="card-back" aria-label="Card reverse with contact details">
    <h1 class="card-back__name">Maren Joy Whitcombe</h1>
    <p class="card-back__contact">
      <span class="email">info@marenwhitcombe.example</span><span class="divider">|</span><span class="website">www.marenwhitcombe.example</span>
    </p>
    <ul class="social-list">
      <li class="social-list__item"><span class="social-list__mark"></span>/MarenWhitcombe</li>
      <li class="social-list__item"><span class="social-list__mark"></span>@MarenJoy</li>
      <li class="social-list__item"><span class="social-list__mark"></span>/MarenWhitcombe</li>
    </ul>
  </section>

  <section class="card-front" aria-label="Card front">
    <div class="card-front__portrait" role="img" aria-label="Black and white headshot portrait of the actress, hands framing her face"></div>
    <p class="card-front__name">Maren<br>Joy<br>Whitcombe</p>
  </section>

</body>
</html>
```